Quimby's Yard & Garden Center Business Card Update

I need an updated Business card design for my Lawn and Garden Center. We do Landscaping installs, Lawn Mowing, Snow Removal and also have a Garden Center Retail Division. I uploaded a few of our previous business cards to give an idea of what we are starting with. The main goal of this update is to simplify and modernize the business card, not all of the services that are on the previous cards has to be on the new one but I would still like to highlight our main services. There is also a sample of our logo that Can be used in the design.

Industry/Entity Type

Landscaping

Contact Information for Business Card

Morris Quimby
Morris@Quimbysyardandgarden.example
Business (555) 201-7784
Cell (555) 318-6092

Colors

Designer to choose colors to be used in the design.

Requirements
Must have
• Services Provided :
• Landscaping
• Lawn Maintenance
• Snow Removal
• Garden Center

```html
<!DOCTYPE html>
<html lang="en">
<head>
<meta charset="utf-8">
<title>Quimby's Yard &amp; Garden Center – Business Card</title>
<link href="https://fonts.googleapis.com/css2?family=Open+Sans:wght@400;600;700&display=swap" rel="stylesheet">
<style>
  :root {
    --brand-green: #2c5a27;
    --card-white: #ffffff;
    --ink: #1f1f1f;
    --rule: #c9c9c9;
    --backdrop: #e6e6e4;
  }
  * { box-sizing: border-box; margin: 0; padding: 0; }
  html, body { width: 1200px; height: 1015px; overflow: hidden; }
  body {
    background: var(--backdrop);
    font-family: "Open Sans", Arial, sans-serif;
    color: var(--ink);
    display: flex;
    flex-direction: column;
    align-items: center;
    justify-content: center;
    gap: 55px;
  }
  .card {
    width: 700px;
    height: 400px;
    box-shadow: 0 8px 24px rgba(0,0,0,.18);
    position: relative;
    overflow: hidden;
  }

  /* Front */
  .card-front {
    background: var(--brand-green);
    display: flex;
    align-items: center;
    justify-content: center;
  }
  .front-wordmark {
    color: var(--card-white);
    font-weight: 700;
    font-size: 84px;
    letter-spacing: 1px;
  }

  /* Back */
  .card-back { background: var(--card-white); }
  .back-body {
    position: absolute;
    inset: 0 0 92px 0;
    display: flex;
    align-items: center;
  }
  .brand-block {
    width: 300px;
    display: flex;
    align-items: center;
    justify-content: center;
    gap: 12px;
  }
  .brand-dot {
    width: 22px; height: 22px;
    border-radius: 50%;
    background: var(--brand-green);
  }
  .brand-name {
    font-weight: 700;
    font-size: 40px;
    color: var(--brand-green);
  }
  .divider {
    width: 1px;
    height: 180px;
    background: var(--rule);
  }
  .contact-block { padding-left: 30px; }
  .person-name {
    color: var(--brand-green);
    font-weight: 700;
    font-size: 19px;
    text-transform: uppercase;
    margin-bottom: 10px;
  }
  .contact-list { list-style: none; font-size: 15px; line-height: 1.45; }
  .contact-list li { display: flex; align-items: center; gap: 7px; }
  .contact-icon {
    width: 15px; height: 15px;
    background: var(--brand-green);
    border-radius: 3px;
    display: inline-flex;
    align-items: center;
    justify-content: center;
    flex: none;
  }
  .address { font-size: 15px; line-height: 1.4; margin-top: 14px; }

  .services-band {
    position: absolute;
    left: 0; right: 0; bottom: 0;
    height: 92px;
    background: var(--brand-green);
    color: var(--card-white);
    display: flex;
    align-items: center;
    justify-content: center;
    gap: 8px;
    font-size: 17px;
  }
  .service-sep {
    width: 10px; height: 10px;
    border-radius: 50%;
    background: var(--card-white);
  }
</style>
</head>
<body>

  <section class="card card-front" aria-label="Card front">
    <span class="front-wordmark">Quimby's</span>
  </section>

  <section class="card card-back" aria-label="Card back">
    <div class="back-body">
      <div class="brand-block">
        <span class="brand-dot"></span>
        <span class="brand-name">Quimby's</span>
      </div>
      <div class="divider"></div>
      <div class="contact-block">
        <h1 class="person-name">Morris Quimby</h1>
        <ul class="contact-list">
          <li>
            <span class="contact-icon">
              <svg width="10" height="10" viewBox="0 0 24 24"><path fill="#fff" d="M6.6 10.8a15 15 0 0 0 6.6 6.6l2.2-2.2a1 1 0 0 1 1-.25 11.4 11.4 0 0 0 3.6.57 1 1 0 0 1 1 1V20a1 1 0 0 1-1 1A17 17 0 0 1 3 4a1 1 0 0 1 1-1h3.5a1 1 0 0 1 1 1c0 1.25.2 2.45.57 3.57a1 1 0 0 1-.25 1z"/></svg>
            </span>(555) 201-7784
          </li>
          <li>
            <span class="contact-icon">
              <svg width="9" height="11" viewBox="0 0 9 11"><rect x="1" y="0.5" width="7" height="10" rx="1.2" fill="none" stroke="#fff" stroke-width="1.2"/></svg>
            </span>(555) 318-6092
          </li>
          <li>
            <span class="contact-icon">
              <svg width="10" height="8" viewBox="0 0 10 8"><rect x="0.6" y="0.6" width="8.8" height="6.8" fill="none" stroke="#fff" stroke-width="1.1"/><path d="M0.6 0.8 5 4.4 9.4 0.8" fill="none" stroke="#fff" stroke-width="1.1"/></svg>
            </span>Morris@Quimbysyardandgarden.example
          </li>
        </ul>
        <p class="address">Quimby's Yard &amp; Garden Center<br>48 Meadow Lane, Fairview, OH 45000</p>
      </div>
    </div>
    <div class="services-band">
      <span>Landscaping</span><span class="service-sep"></span>
      <span>Lawn Maintenance</span><span class="service-sep"></span>
      <span>Snow Removal</span><span class="service-sep"></span>
      <span>Garden Center</span>
    </div>
  </section>

</body>
</html>
```